Christmas Card for Holidays to Companies Clients

Hello designers! We are looking for the best Christmas Cards we can get to send out to our companies clients in the holidays. We don't have a lot of specifications, we just wanted to have a little detail with them for the upcoming holidays.

Our company is a technological company that offers different product, solutions and services. Most of our clients are some of the countries banks.

Colors

Designer to choose colors to be used in the design.

Requirements
Must have
• The logo and name of our company (Solvanek) and a nice but short and precise message for the holidays.

```html
<!DOCTYPE html>
<html lang="en">
<head>
<meta charset="utf-8">
<title>Solvanek Holiday Card</title>
<link rel="stylesheet" href="https://fonts.googleapis.com/css2?family=Dancing+Script:wght@600&family=Montserrat:wght@500;700&family=Questrial&display=swap">
<style>
  :root {
    --stage: #e9e3da;
    --wood-dark: #2a170c;
    --wood-mid: #5a3218;
    --wood-warm: #8a5226;
    --glow: #ffd58a;
    --frame-light: #d8bb92;
    --frame-dark: #a07a4e;
    --chalk-board: #1b1d1d;
    --chalk: #e6e6e2;
    --badge: #ffffff;
    --brand: #3a3a3c;
    --brand-sub: #6a6a6a;
    --gold: #e8b64a;
    --url: #ffffff;
  }
  * { margin: 0; padding: 0; box-sizing: border-box; }
  html, body { width: 1200px; height: 800px; overflow: hidden; background: var(--stage); }
  .holiday-card {
    position: absolute; left: 233px; top: 33px;
    width: 734px; height: 734px; overflow: hidden;
    box-shadow: 0 6px 18px rgba(0,0,0,.25);
  }
  .card-photo {
    position: absolute; inset: 0;
    background:
      radial-gradient(ellipse 60% 30% at 45% 18%, rgba(255,200,120,.55), transparent 70%),
      radial-gradient(circle at 88% 12%, rgba(40,80,40,.85) 0 12%, transparent 24%),
      radial-gradient(ellipse 70% 55% at 50% 40%, var(--wood-warm), transparent 80%),
      linear-gradient(180deg, var(--wood-mid), var(--wood-dark));
  }
  .chalkboard {
    position: absolute; left: 166px; top: 274px; width: 392px; height: 328px;
    background: linear-gradient(135deg, var(--frame-light), var(--frame-dark));
    box-shadow: 0 4px 10px rgba(0,0,0,.45);
  }
  .chalkboard-surface {
    position: absolute; left: 32px; top: 32px; right: 32px; bottom: 36px;
    background: var(--chalk-board);
  }
  .brand-badge {
    position: absolute; left: 84px; top: 45px; width: 224px; height: 66px;
    background: var(--badge); border-radius: 2px;
    display: flex; flex-direction: column; justify-content: center; align-items: center;
  }
  .brand-name {
    font-family: "Montserrat", sans-serif; font-weight: 700;
    font-size: 22px; letter-spacing: .5px; color: var(--brand); line-height: 1;
  }
  .brand-tagline {
    font-family: "Montserrat", sans-serif; font-weight: 500;
    font-size: 7.5px; letter-spacing: .4px; color: var(--brand-sub); margin-top: 4px;
  }
  .greeting {
    position: absolute; left: 32px; right: 32px; top: 146px;
    font-family: "Dancing Script", cursive; font-weight: 600;
    font-size: 31px; line-height: 39px; color: var(--chalk);
    text-align: center;
  }
  .web-link {
    position: absolute; left: 183px; top: 661px; width: 368px; height: 46px;
    border: 2px solid var(--gold);
    display: flex; align-items: center; justify-content: center;
    font-family: "Questrial", sans-serif; font-size: 21px; letter-spacing: .5px;
    color: var(--url);
  }
</style>
</head>
<body>
  <div class="holiday-card">
    <div class="card-photo" role="img" aria-label="Dark wooden table with glowing string fairy lights, a twine loop, and holly with pine cones and red berries in the top right corner"></div>
    <div class="chalkboard">
      <div class="chalkboard-surface"></div>
      <div class="brand-badge">
        <span class="brand-name">SOLVANEK</span>
        <span class="brand-tagline">IT CONSULTING AND SERVICES</span>
      </div>
      <p class="greeting">Wishing you a very happy<br>Holiday season and a<br>wonderful New Year!</p>
    </div>
    <div class="web-link">www.solvanek.com.do</div>
  </div>
</body>
</html>
```